Stationery Design Project

We are interested in A4 paper letterheads, envelopes, maybe A4 folders where we can put the patients' results in and businesscards. No information will be given out for the time being.
We would like to see mainly shades of white.. please refer to
http://en.brivola.org/wiki/Category:Tints_of_pale
anti-flash white, splashed white,ghost white, ivory, snow and white smoke or even light grey
we are interested mainly on the silver design but we welcome the other colors as well. Since its about a gynecologist please avoid dark colors, instead use shades of beige, light grey and white

```html
<!DOCTYPE html>
<html lang="en">
<head>
<meta charset="utf-8">
<title>Folder – Outside Spread</title>
<link href="https://fonts.googleapis.com/css2?family=PT+Sans+Narrow:wght@400;700&display=swap" rel="stylesheet">
<style>
  :root {
    --page: #ffffff;
    --olive: #bfbf99;
    --olive-faint: #cdcdac;
    --fold-line: #9a9a7a;
    --band: #e4e4d4;
    --heading: #7a6a5e;
    --body-text: #7a6a5e;
    --back-text: #ffffff;
    --mark: #6f8a8c;
  }
  * { margin: 0; padding: 0; box-sizing: border-box; }
  html, body {
    width: 1200px;
    height: 848px;
    overflow: hidden;
    background: var(--page);
  }
  .canvas {
    position: relative;
    width: 1200px;
    height: 848px;
    font-family: "PT Sans Narrow", "Arial Narrow", sans-serif;
  }
  .folder {
    position: absolute;
    left: 98px;
    top: 63px;
    width: 1002px;
    height: 721px;
    background: var(--olive);
    overflow: hidden;
  }
  .back-watermark {
    position: absolute;
    left: 18px;
    top: 170px;
    color: var(--olive-faint);
    font-size: 190px;
    font-weight: 400;
    line-height: 1;
    letter-spacing: 2px;
    white-space: nowrap;
  }
  .fold {
    position: absolute;
    left: 500px;
    top: 0;
    width: 1px;
    height: 100%;
    background: var(--fold-line);
  }
  .back-note {
    position: absolute;
    left: 40px;
    top: 646px;
    width: 425px;
    color: var(--back-text);
    font-weight: 700;
    font-size: 14px;
    line-height: 18px;
  }
  .cover-band {
    position: absolute;
    left: 624px;
    top: 0;
    width: 255px;
    height: 100%;
    background: var(--band);
  }
  .brand {
    position: absolute;
    left: 0;
    top: 155px;
    width: 100%;
    text-align: center;
    color: var(--mark);
    font-size: 50px;
    font-weight: 400;
    line-height: 1;
    letter-spacing: 2px;
  }
  .cover-title {
    position: absolute;
    left: 16px;
    top: 457px;
    color: var(--heading);
    font-size: 38px;
    font-weight: 400;
    letter-spacing: -0.5px;
    white-space: nowrap;
  }
  .cover-text {
    position: absolute;
    left: 20px;
    top: 515px;
    width: 218px;
    color: var(--body-text);
    font-size: 17px;
    font-weight: 700;
    line-height: 24px;
    text-align: justify;
  }
</style>
</head>
<body>
  <main class="canvas">
    <section class="folder">
      <div class="back-panel">
        <p class="back-watermark" aria-hidden="true">Belvara</p>
        <p class="back-note">Some text here Ad que nonse enimpor ersped quam si odic tem aperchi cienitate dolorepuda corunt et doluptiat laut</p>
      </div>
      <div class="fold"></div>
      <div class="cover-band">
        <p class="brand">Belvara</p>
        <h1 class="cover-title">SOME TEXT HERE</h1>
        <p class="cover-text">Some text here Ad que nonse enimpor ersped quam si odic tem aperchi cienitate dolorepuda corunt et doluptiat laut</p>
      </div>
    </section>
  </main>
</body>
</html>
```